Letterhead, stationery and email signature for construction business

I need the letterhead, stationery and email signature designs for a construction business. I want them to have a corporate feel to them.

I've attached the logo for reference.

```html
<!DOCTYPE html>
<html lang="en">
<head>
<meta charset="utf-8">
<title>Corvane Projects – Stationery Suite</title>
<link rel="stylesheet" href="https://fonts.googleapis.com/css2?family=Mulish:wght@300;400;600;700;800&display=swap">
<style>
  :root{
    --brand-blue:#2c58a3;
    --band-grey:#50505a;
    --ink:#1b1b1f;
    --frame:#2a2a2e;
    --paper:#ffffff;
    --tint-grey:#efeff1;
    --tint-blue:#e7edf6;
    --photo-warm:#c9b08a;
    --photo-dark:#6b5a45;
  }
  *{box-sizing:border-box;margin:0;padding:0}
  html,body{width:1200px;height:775px;overflow:hidden;background:var(--paper)}
  body{position:relative;font-family:"Mulish",sans-serif;color:var(--ink)}

  .piece-label{position:absolute;font-size:13px;font-weight:400;color:var(--ink);letter-spacing:.2px}
  .piece{position:absolute;background:var(--paper);border:1px solid var(--frame);overflow:hidden}
  .bands{position:absolute;inset:0;width:100%;height:100%}
  .blue{fill:var(--brand-blue)}
  .grey{fill:var(--band-grey)}

  .wordmark{position:absolute;display:flex;align-items:center;gap:4px;color:var(--brand-blue);font-weight:800;white-space:nowrap;letter-spacing:.4px}
  .wordmark .mark-square{display:inline-block;flex:none;background:var(--brand-blue)}
  .wordmark .name{display:block;line-height:1.02}

  .contact{position:absolute;font-size:7px;line-height:1.25;white-space:nowrap}
  .contact p+p{margin-top:7px}
  .contact .web,.contact.web{font-weight:700}

  /* Letterhead */
  .letterhead{left:61px;top:109px;width:419px;height:592px}
  .letterhead .wordmark{left:257px;top:28px;font-size:13px}
  .letterhead .wordmark .mark-square{width:26px;height:26px}
  .letterhead .contact{left:257px;top:69px}
  .watermark-block{position:absolute;left:0;top:131px;width:258px;height:282px;background:linear-gradient(135deg,var(--tint-grey),var(--tint-blue))}

  /* Envelopes */
  .envelope-back{left:697px;top:84px;width:411px;height:206px}
  .envelope-front-flap{position:absolute;left:543px;top:159px;width:413px;height:56px}
  .envelope-front{left:543px;top:214px;width:413px;height:206px}
  .envelope-front .wordmark{left:23px;top:145px;font-size:11px}
  .envelope-front .wordmark .mark-square{width:22px;height:22px}
  .envelope-front .contact{font-size:5.5px;top:159px}
  .envelope-front .col-address{left:139px}
  .envelope-front .col-phone{left:223px}
  .envelope-front .col-web{left:317px;top:166px}

  /* Email signature */
  .signature{left:177px;top:493px;width:590px;height:151px}
  .portrait-backing{position:absolute;left:26px;top:0;width:116px;height:96px;background:var(--brand-blue);border-radius:0 0 8px 8px}
  .portrait{position:absolute;left:24px;top:8px;width:140px;height:143px;background:linear-gradient(180deg,var(--photo-warm),var(--photo-dark));border-radius:60px 60px 0 0}
  .sig-name{position:absolute;left:168px;top:18px;font-size:22px;line-height:1;letter-spacing:.2px;white-space:nowrap}
  .sig-name b{font-weight:700}
  .sig-name span{font-weight:300}
  .sig-title{position:absolute;left:170px;top:44px;font-size:15px;font-weight:300;letter-spacing:.2px}
  .signature .wordmark{left:462px;top:20px;font-size:10.5px}
  .signature .wordmark .mark-square{width:20px;height:20px}
  .sig-line{position:absolute;display:flex;align-items:center;gap:8px;font-size:7px;font-weight:600;white-space:nowrap}
  .sig-line svg{width:12px;height:12px;fill:var(--brand-blue)}

  /* Name cards */
  .card-back{left:796px;top:441px;width:253px;height:154px}
  .card-back .wordmark{left:62px;top:52px;font-size:16px;gap:6px}
  .card-back .wordmark .mark-square{width:32px;height:32px}
  .card-front{left:884px;top:547px;width:252px;height:154px}
  .card-front .wordmark{left:134px;top:18px;font-size:10px}
  .card-front .wordmark .mark-square{width:20px;height:20px}
  .card-person{position:absolute;left:17px;top:47px;line-height:1.15;white-space:nowrap}
  .card-person .name{font-size:8px;font-weight:700}
  .card-person .role{font-size:5.5px;font-weight:700}
  .card-person .mobile{font-size:7.5px;font-weight:700}
  .card-front .contact{left:17px;top:86px;font-size:6.5px}
  .card-front .card-web{position:absolute;right:28px;top:120px;font-size:6.5px;font-weight:700;white-space:nowrap}
</style>
</head>
<body>

  <!-- Letterhead -->
  <div class="piece-label" style="left:62px;top:89px">Letterhead</div>
  <section class="piece letterhead">
    <svg class="bands" viewBox="0 0 419 592" preserveAspectRatio="none" aria-hidden="true">
      <polygon class="blue" points="399,0 419,0 419,592 399,567"/>
      <polygon class="grey" points="0,572 386,572 401,592 0,592"/>
    </svg>
    <div class="watermark-block" aria-hidden="true"></div>
    <div class="wordmark"><i class="mark-square"></i><span class="name">CORVANE<br>PROJECTS</span></div>
    <div class="contact">
      <p>48 Harbour Rd., Eastmere City<br>Coastal State 4400 Australia.</p>
      <p>(08) 5550 1827<br>service@corvane.example</p>
      <p class="web" style="margin-top:13px">corvane.example</p>
    </div>
  </section>

  <!-- DL Envelope -->
  <section class="piece envelope-back">
    <svg class="bands" viewBox="0 0 411 206" preserveAspectRatio="none" aria-hidden="true">
      <path class="blue" d="M0,0 H411 L374,47 Q370,53 360,53 H50 Q40,53 36,47 Z"/>
    </svg>
  </section>
  <svg class="envelope-front-flap" viewBox="0 0 413 56" aria-hidden="true">
    <path class="blue" d="M0.5,55.5 L36,8 Q41,2 50,2 H360 Q369,2 374,8 L412.5,55.5 Z" stroke="#2a2a2e" stroke-width="1"/>
  </svg>
  <section class="piece envelope-front">
    <svg class="bands" viewBox="0 0 413 206" preserveAspectRatio="none" aria-hidden="true">
      <polygon class="blue" points="393,0 413,0 413,206 393,182"/>
      <polygon class="grey" points="0,187 380,187 394,206 0,206"/>
    </svg>
    <div class="wordmark"><i class="mark-square"></i><span class="name">CORVANE<br>PROJECTS</span></div>
    <div class="contact col-address">48 Harbour Rd., Eastmere City<br>Coastal State 4400 Australia</div>
    <div class="contact col-phone">(08) 5550 1827<br>service@corvane.example</div>
    <div class="contact col-web web">corvane.example</div>
  </section>
  <div class="piece-label" style="left:1033px;top:297px">DL Envelope</div>

  <!-- Name cards -->
  <section class="piece card-back">
    <svg class="bands" viewBox="0 0 253 154" preserveAspectRatio="none" aria-hidden="true">
      <polygon class="blue" points="240,0 253,0 253,154 240,141"/>
      <polygon class="grey" points="0,141 228,141 240,154 0,154"/>
    </svg>
    <div class="wordmark"><i class="mark-square"></i><span class="name">CORVANE<br>PROJECTS</span></div>
  </section>
  <section class="piece card-front">
    <svg class="bands" viewBox="0 0 252 154" preserveAspectRatio="none" aria-hidden="true">
      <polygon class="blue" points="239,0 252,0 252,154 239,140"/>
      <polygon class="grey" points="0,141 230,141 241,154 0,154"/>
    </svg>
    <div class="wordmark"><i class="mark-square"></i><span class="name">CORVANE<br>PROJECTS</span></div>
    <div class="card-person">
      <div class="name">Daniel Whitmore</div>
      <div class="role">Project Manager</div>
      <div class="mobile">0400 555 318</div>
    </div>
    <div class="contact">
      <p>48 Harbour Rd., Eastmere City<br>Coastal State 4400 Australia.</p>
      <p>(08) 5550 1827<br>service@corvane.example</p>
    </div>
    <div class="card-web">corvane.example</div>
  </section>
  <div class="piece-label" style="left:1066px;top:707px">Name Card</div>

  <!-- Email signature -->
  <section class="piece signature">
    <svg class="bands" viewBox="0 0 590 151" preserveAspectRatio="none" aria-hidden="true">
      <polygon class="blue" points="566,0 590,0 590,151 566,121"/>
      <polygon class="grey" points="0,128 552,128 568,151 0,151"/>
    </svg>
    <div class="portrait-backing" aria-hidden="true"></div>
    <div class="portrait" role="img" aria-label="Portrait photo of the project manager"></div>
    <h1 class="sig-name"><b>DANIEL</b> <span>WHITMORE</span></h1>
    <div class="sig-title">PROJECT MANAGER</div>
    <div class="wordmark"><i class="mark-square"></i><span class="name">CORVANE<br>PROJECTS</span></div>
    <div class="sig-line" style="left:168px;top:78px">
      <svg viewBox="0 0 24 24" aria-hidden="true"><path d="M2 5h20v14H2z M3.5 6.5 12 13l8.5-6.5" fill="none" stroke="#2c58a3" stroke-width="2"/></svg>
      d.whitmore@corvane.example
    </div>
    <div class="sig-line" style="left:168px;top:95px">
      <svg viewBox="0 0 24 24" aria-hidden="true"><path d="M6.6 10.8a15 15 0 0 0 6.6 6.6l2.2-2.2a1 1 0 0 1 1-.25 11.4 11.4 0 0 0 3.6.57 1 1 0 0 1 1 1V20a1 1 0 0 1-1 1A17 17 0 0 1 3 4a1 1 0 0 1 1-1h3.5a1 1 0 0 1 1 1c0 1.25.2 2.45.57 3.57a1 1 0 0 1-.25 1z"/></svg>
      0400 555 318
    </div>
    <div class="sig-line" style="left:335px;top:80px">
      <svg viewBox="0 0 24 24" aria-hidden="true"><path d="M12 2a7 7 0 0 0-7 7c0 5.2 7 13 7 13s7-7.8 7-13a7 7 0 0 0-7-7zm0 9.5A2.5 2.5 0 1 1 12 6.5a2.5 2.5 0 0 1 0 5z"/></svg>
      48 Harbour Rd., Eastmere City, Coastal State 4400 Australia.
    </div>
    <div class="sig-line" style="left:335px;top:96px">
      <svg viewBox="0 0 24 24" aria-hidden="true"><circle cx="12" cy="12" r="9" fill="none" stroke="#2c58a3" stroke-width="2"/><path d="M3 12h18M12 3c3 3 3 15 0 18M12 3c-3 3-3 15 0 18" fill="none" stroke="#2c58a3" stroke-width="1.6"/></svg>
      corvane.example
    </div>
  </section>
  <div class="piece-label" style="left:622px;top:649px">Email Signature Designs</div>

</body>
</html>
```